Basic Company webpage with the elements and colors of our Logo

Basic Home page with a few pages:
- Home,
- About US,
- Contact us
- Services

Target Market(s)

Business Customers (B2B)

Coding

Coded - Design and coding required

Number of Pages Required

5+ page

Requirements
Must have
• Professional, Clean, Simple High Tech, Contact should have a contact us dialog for sending messages to us
Nice to have
• Meet with us links for calendar access though MS Bookings

```html
<!DOCTYPE html>
<html lang="en">
<head>
<meta charset="utf-8">
<title>Vertex Systems Group</title>
<link href="https://fonts.googleapis.com/css2?family=Montserrat:wght@400;500;600;700;800&display=swap" rel="stylesheet">
<style>
:root{
  --blue:#13607f;
  --blue-dark:#0d4a66;
  --orange:#f4b35a;
  --ink:#2d3a44;
  --white:#ffffff;
  --line:#e3e3e3;
}
*{box-sizing:border-box;margin:0;padding:0}
html,body{width:1200px;height:4655px;overflow:hidden}
body{position:relative;font-family:'Montserrat',sans-serif;color:var(--ink);background:var(--white)}
.abs{position:absolute}
.bg-svg{position:absolute;left:0;top:0}
.brand{position:absolute;left:70px;top:44px;display:flex;align-items:center;gap:10px}
.brand-dot{width:22px;height:22px;border-radius:50%;background:var(--orange)}
.brand-name{font-weight:800;font-size:25px;color:var(--blue);letter-spacing:.5px}
.topbar-quote{position:absolute;left:695px;top:0;width:215px;height:46px;background:var(--orange);display:flex;align-items:center;justify-content:center;gap:12px;font-size:14px;font-weight:600;color:var(--blue-dark)}
.topbar-call{position:absolute;left:908px;top:0;width:292px;height:46px;background:var(--blue);display:flex;align-items:center;justify-content:center;gap:10px;font-size:14px;font-weight:600;color:var(--orange)}
.nav{position:absolute;top:76px;left:440px;display:flex;font-size:14px;font-weight:700;color:var(--blue)}
.nav a{text-decoration:none;color:inherit}
.nav .active{color:var(--orange)}
.hero-photo{position:absolute;left:0;top:122px;width:1200px;height:650px;background:linear-gradient(110deg,#c9ccd0 0%,#8f9aa2 35%,#2f6d86 65%,#134e69 100%)}
.hero-title{position:absolute;left:713px;top:262px;font-size:47px;line-height:54px;font-weight:800;color:var(--white)}
.hero-call{position:absolute;left:713px;top:458px;display:flex;align-items:center;gap:16px;color:var(--white)}
.round-icon{width:58px;height:58px;border-radius:50%;background:var(--orange);display:flex;align-items:center;justify-content:center}
.hero-call p{font-size:28px;font-weight:700;line-height:28px}
.dots{position:absolute;left:30px;top:382px;display:flex;flex-direction:column;gap:14px}
.dots span{width:7px;height:7px;border-radius:50%;background:#fff}
.dots .on{background:transparent;border:2px solid var(--orange);width:11px;height:11px;margin-left:-2px}
.h2{font-weight:800;font-size:44px;color:var(--blue);line-height:1}
.body-text{font-size:15px;line-height:22px}
.btn{position:absolute;background:var(--blue);color:#fff;font-size:14px;font-weight:700;display:flex;align-items:center;justify-content:center}
.about-photo{position:absolute;left:114px;top:811px;width:422px;height:422px;border-radius:50%;background:radial-gradient(circle at 40% 40%,#8c9aa6,#2b4756)}
.why-list{position:absolute;left:128px;top:1688px;list-style:none;font-size:16px;line-height:22px;width:380px}
.why-list li{position:relative;padding-left:30px;margin-bottom:20px}
.why-list li::before{content:"";position:absolute;left:2px;top:7px;width:9px;height:9px;border-radius:50%;background:var(--orange)}
.why-photo{position:absolute;left:677px;top:1533px;width:396px;height:494px;background:linear-gradient(160deg,#d4d7d9,#8b8477 60%,#6b655c)}
.services-bg{position:absolute;left:0;top:2180px;width:1200px;height:680px}
.card{position:absolute;top:2390px;width:220px;height:310px;background:#fff;text-align:center;padding-top:30px}
.card.hl{background:var(--orange)}
.card-icon{width:118px;height:118px;border-radius:50%;border:5px solid var(--orange);background:var(--blue);margin:0 auto;display:flex;align-items:center;justify-content:center}
.card.hl .card-icon{border-color:#fff}
.card h3{margin-top:22px;font-size:15px;font-weight:700;color:var(--blue);line-height:21px}
.card.hl h3{color:#fff}
.card p{margin:12px auto 0;width:160px;font-size:13px;line-height:20px;color:#444}
.card.hl p{color:#fff}
.post{position:absolute;top:3080px;width:294px;height:433px;border:1px solid var(--line);background:#fff}
.post-img{height:260px}
.post h3{margin:20px 26px 0;font-size:16px;line-height:21px;font-weight:700;color:var(--blue)}
.post p{margin:14px 26px 0;font-size:14px;line-height:19px;color:#666}
.post a{display:block;margin:16px 28px 0;font-size:14px;font-weight:700;color:var(--orange);text-decoration:none}
.cta-title{position:absolute;left:128px;top:3745px;font-size:34px;line-height:45px;font-weight:800;color:#fff}
.field{position:absolute;border:1px solid rgba(255,255,255,.8);background:rgba(255,255,255,.15);font-size:13px;color:#fff;padding:16px 0 0 16px}
.foot-h{position:absolute;top:4288px;font-size:20px;font-weight:600;color:#fff}
.foot-list{position:absolute;top:4335px;list-style:none;font-size:14px;line-height:28px;color:#fff}
.foot-contact{position:absolute;left:883px;display:flex;gap:18px;align-items:center;color:#fff;font-size:14px;line-height:19px}
.social{position:absolute;left:112px;top:4480px;display:flex;gap:18px}
.social span{width:22px;height:22px;border-radius:50%;background:var(--orange)}
</style>
</head>
<body>

<svg class="bg-svg" width="1200" height="4655" viewBox="0 0 1200 4655" aria-hidden="true">
  <path d="M0 560 C250 610 600 800 1200 615 L1200 1170 C900 1310 500 1380 0 1240 Z" fill="var(--orange)"/>
  <rect x="0" y="3620" width="1200" height="600" fill="var(--orange)"/>
  <path d="M0 4000 C350 3960 650 4200 1200 4160 L1200 4655 L0 4655 Z" fill="var(--blue)"/>
  <path d="M0 4000 C350 3960 650 4200 1200 4160" fill="none" stroke="#fff" stroke-width="4"/>
</svg>

<header>
  <div class="brand"><span class="brand-dot"></span><span class="brand-name">VERTEX SYSTEMS</span></div>
  <div class="topbar-quote">GET A QUOTE
    <svg width="16" height="16" viewBox="0 0 16 16"><circle cx="8" cy="8" r="8" fill="var(--blue-dark)"/><path d="M5 8h6M8.5 5.5 11 8l-2.5 2.5" stroke="var(--orange)" stroke-width="1.8" fill="none"/></svg>
  </div>
  <div class="topbar-call">
    <svg width="16" height="16" viewBox="0 0 24 24"><path d="M6.6 10.8a15 15 0 0 0 6.6 6.6l2.2-2.2c.3-.3.7-.4 1-.2 1.1.4 2.3.6 3.6.6.6 0 1 .4 1 1V20c0 .6-.4 1-1 1A17 17 0 0 1 3 4c0-.6.4-1 1-1h3.5c.6 0 1 .4 1 1 0 1.3.2 2.5.6 3.6.1.3 0 .7-.2 1z" fill="var(--orange)"/></svg>
    CALL: 067 555 0142
  </div>
  <nav class="nav">
    <a class="active" style="width:105px">HOME</a>
    <a style="width:135px">SERVICES</a>
    <a style="width:175px">TESTIMONIALS</a>
    <a style="width:190px">WHY CHOOSE US</a>
    <a>GALLERY</a>
  </nav>
</header>

<section class="hero">
  <div class="hero-photo" role="img" aria-label="Two colleagues in an office reviewing a tablet"></div>
  <svg class="abs" style="left:0;top:520px" width="1200" height="260" viewBox="0 520 1200 260" aria-hidden="true">
    <path d="M0 540 C250 600 500 790 820 760 C1000 740 1100 680 1200 620 L1200 640 C1100 700 1000 765 820 776 C500 800 250 620 0 565 Z" fill="var(--blue-dark)"/>
    <path d="M0 565 C250 620 500 800 820 776 C1000 765 1100 700 1200 640 L1200 780 L0 780 Z" fill="var(--orange)"/>
  </svg>
  <div class="dots"><span></span><span class="on"></span><span></span><span></span></div>
  <h1 class="hero-title">DALE PORTER<br>HANDYMAN<br>SERVICES</h1>
  <div class="hero-call">
    <div class="round-icon"><svg width="26" height="26" viewBox="0 0 24 24"><path d="M6.6 10.8a15 15 0 0 0 6.6 6.6l2.2-2.2c.3-.3.7-.4 1-.2 1.1.4 2.3.6 3.6.6.6 0 1 .4 1 1V20c0 .6-.4 1-1 1A17 17 0 0 1 3 4c0-.6.4-1 1-1h3.5c.6 0 1 .4 1 1 0 1.3.2 2.5.6 3.6.1.3 0 .7-.2 1z" fill="#fff"/></svg></div>
    <p>CALL US<br>985 555 0176</p>
  </div>
</section>

<section class="about">
  <div class="about-photo" role="img" aria-label="Two smiling business partners standing side by side"></div>
  <h2 class="h2 abs" style="left:575px;top:895px">ABOUT US</h2>
  <p class="body-text abs" style="left:575px;top:962px;width:405px;color:#3a3a3a">Lorem ipsum dolor sit amet, consectetur adipiscing elit, sed do eiusmod tempor incididunt ut labore et dolore magna aliqua. Quis ipsum suspendisse ultrices gravida. Risus commodo viverra maecenas accumsan lacus vel facilisis.</p>
  <div class="btn" style="left:575px;top:1100px;width:148px;height:50px">READ MORE</div>
</section>

<section class="why">
  <h2 class="h2 abs" style="left:128px;top:1515px">WHY CHOOSE US?</h2>
  <p class="body-text abs" style="left:128px;top:1582px;width:455px;color:#222">Lorem ipsum dolor sit amet, consectetur adipiscing elit, sed do eiusmod tempor incididunt ut labore et dolore magna aliqua. Quis ipsum suspendisse ultrices gravida.</p>
  <ul class="why-list">
    <li>Lorem ipsum dolor sit amet, consectetur adipiscing elit, sed do eiusmod</li>
    <li>tempor incididunt ut labore et dolore magna aliqua.</li>
    <li>Quis ipsum suspendisse ultrices gravida.</li>
    <li>Risus commodo viverra maecenas acc umsan lacus vel facilisis.</li>
  </ul>
  <div class="btn" style="left:128px;top:1952px;width:147px;height:52px">READ MORE</div>
  <div class="why-photo" role="img" aria-label="Smiling businessman in a suit holding a tablet"></div>
</section>

<section>
  <svg class="services-bg" viewBox="0 0 1200 680" aria-hidden="true">
    <defs><linearGradient id="svc" x1="0" y1="0" x2="1" y2="0"><stop offset="0" stop-color="#2a6d88"/><stop offset=".5" stop-color="#15607f"/><stop offset="1" stop-color="#1c6584"/></linearGradient></defs>
    <path d="M0 90 C300 -10 900 -10 1200 90 L1200 600 C900 690 300 690 0 600 Z" fill="url(#svc)"/>
    <path d="M0 90 C300 -10 900 -10 1200 90" fill="none" stroke="var(--orange)" stroke-width="12"/>
    <path d="M0 600 C300 690 900 690 1200 600" fill="none" stroke="var(--orange)" stroke-width="12"/>
  </svg>
  <h2 class="h2 abs" style="left:0;width:1200px;text-align:center;top:2295px;color:#fff">OUR SERVICES</h2>

  <div class="card hl" style="left:125px">
    <div class="card-icon"><svg width="54" height="54" viewBox="0 0 54 54" fill="none" stroke="#fff" stroke-width="2.5"><circle cx="27" cy="20" r="8"/><path d="M10 46v-6a8 8 0 0 1 8-8h18a8 8 0 0 1 8 8v6Z"/></svg></div>
    <h3>DOLOR SIT AMET<br>ADIPISCING</h3>
    <p>Lorem ipsum dolor sit amet, consectetur adipi scing elit, sed do eius.</p>
  </div>
  <div class="card" style="left:368px">
    <div class="card-icon"><svg width="54" height="54" viewBox="0 0 54 54" fill="none" stroke="#fff" stroke-width="2.5"><circle cx="27" cy="27" r="16"/><path d="M19 32l6-6 5 4 7-9"/></svg></div>
    <h3>DOLOR SIT AMET<br>ADIPISCING</h3>
    <p>Lorem ipsum dolor sit amet, consectetur adipi scing elit, sed do eius.</p>
  </div>
  <div class="card" style="left:611px">
    <div class="card-icon"><svg width="54" height="54" viewBox="0 0 54 54" fill="none" stroke="#fff" stroke-width="2.5"><path d="M27 10l15 8v18l-15 8-15-8V18Z"/><path d="M12 18l15 8 15-8M27 26v18"/></svg></div>
    <h3>DOLOR SIT AMET<br>ADIPISCING</h3>
    <p>Lorem ipsum dolor sit amet, consectetur adipi scing elit, sed do eius.</p>
  </div>
  <div class="card" style="left:853px">
    <div class="card-icon"><svg width="54" height="54" viewBox="0 0 54 54" fill="none" stroke="#fff" stroke-width="2.5"><circle cx="27" cy="17" r="7"/><path d="M8 34l10-6 9 6 9-6 10 6-10 10H18Z"/></svg></div>
    <h3>DOLOR SIT AMET<br>ADIPISCING</h3>
    <p>Lorem ipsum dolor sit amet, consectetur adipi scing elit, sed do eius.</p>
  </div>
</section>

<section class="blog">
  <h2 class="h2 abs" style="left:0;width:1200px;text-align:center;top:2992px">LATEST BLOG</h2>
  <article class="post" style="left:126px">
    <div class="post-img" role="img" aria-label="Business meeting at a conference table" style="background:linear-gradient(135deg,#6e7b86,#2f3d49)"></div>
    <h3>LOREM IPSUM DOLOR SIT AMET LORE CONSECT</h3>
    <p>Lorem ipsum dolor sit ametco sctetur adipiscing elitsed.</p>
    <a>Read More</a>
  </article>
  <article class="post" style="left:453px">
    <div class="post-img" role="img" aria-label="Open hand under a glowing technology network graphic" style="background:radial-gradient(circle at 50% 45%,#5fa7cc,#173550 70%)"></div>
    <h3>LOREM IPSUM DOLOR SIT AMET LORE CONSECT</h3>
    <p>Lorem ipsum dolor sit ametco sctetur adipiscing elitsed.</p>
    <a>Read More</a>
  </article>
  <article class="post" style="left:780px">
    <div class="post-img" role="img" aria-label="Colleagues shaking hands in a bright office" style="background:linear-gradient(135deg,#9aa8b3,#3f5a73)"></div>
    <h3>LOREM IPSUM DOLOR SIT AMET LORE CONSECT</h3>
    <p>Lorem ipsum dolor sit ametco sctetur adipiscing elitsed.</p>
    <a>Read More</a>
  </article>
</section>

<section class="contact">
  <h2 class="cta-title">LOREM IPSUM DO<br>LOR SIT AMET CONS<br>ECTETUR ADIP.</h2>
  <div class="btn" style="left:128px;top:3898px;width:282px;height:58px;font-size:18px;letter-spacing:.5px">CALENDAR&nbsp; BOOKINGS</div>
  <h2 class="h2 abs" style="left:628px;top:3735px;color:#fff">CONTACT US</h2>
  <div class="field" style="left:628px;top:3790px;width:218px;height:48px">Name:</div>
  <div class="field" style="left:857px;top:3790px;width:216px;height:48px">Email:</div>
  <div class="field" style="left:628px;top:3855px;width:218px;height:48px">Phone:</div>
  <div class="field" style="left:857px;top:3855px;width:216px;height:48px">Subject:</div>
  <div class="field" style="left:628px;top:3918px;width:445px;height:106px">Message:</div>
  <div class="btn" style="left:630px;top:4040px;width:160px;height:46px">SUBMIT NOW</div>
</section>

<footer>
  <div class="brand" style="left:112px;top:4306px"><span class="brand-dot"></span><span class="brand-name" style="color:#fff;font-size:22px">VERTEX SYSTEMS</span></div>
  <p class="abs" style="left:112px;top:4382px;width:220px;font-size:13px;line-height:20px;color:#fff">Lorem ipsum dolor sit amet, con sectetur adipiscing elit, seolord do eiusmod tempor incididunt ut labore et dolore magna.</p>
  <div class="social"><span></span><span></span><span></span></div>

  <h4 class="foot-h" style="left:440px">MENU</h4>
  <ul class="foot-list" style="left:440px"><li>- Home,</li><li>- About US,</li><li>- Contact us</li><li>- Services</li></ul>

  <h4 class="foot-h" style="left:664px">LINKS</h4>
  <ul class="foot-list" style="left:664px"><li>Privacy Policy</li><li>Terms &amp; Conditions</li><li>Sitemap</li><li>Case Studies</li><li>Testimonials</li></ul>

  <h4 class="foot-h" style="left:883px">CONTACT</h4>
  <div class="foot-contact" style="top:4338px">
    <div class="round-icon" style="width:40px;height:40px"><svg width="18" height="18" viewBox="0 0 24 24"><path d="M12 2a7 7 0 0 0-7 7c0 5 7 13 7 13s7-8 7-13a7 7 0 0 0-7-7zm0 9.5A2.5 2.5 0 1 1 12 6.5a2.5 2.5 0 0 1 0 5z" fill="#fff"/></svg></div>
    <p>Lorem Dummyloac<br>Lor 345 Pind 338</p>
  </div>
  <div class="foot-contact" style="top:4398px">
    <div class="round-icon" style="width:40px;height:40px"><svg width="18" height="18" viewBox="0 0 24 24"><path d="M6.6 10.8a15 15 0 0 0 6.6 6.6l2.2-2.2c.3-.3.7-.4 1-.2 1.1.4 2.3.6 3.6.6.6 0 1 .4 1 1V20c0 .6-.4 1-1 1A17 17 0 0 1 3 4c0-.6.4-1 1-1h3.5c.6 0 1 .4 1 1 0 1.3.2 2.5.6 3.6.1.3 0 .7-.2 1z" fill="#fff"/></svg></div>
    <p>Phone:<br>673 555 0193</p>
  </div>
  <div class="foot-contact" style="top:4458px">
    <div class="round-icon" style="width:40px;height:40px"><svg width="18" height="18" viewBox="0 0 24 24"><path d="M3 6h18v12H3z" fill="#fff"/><path d="M3 6l9 7 9-7" stroke="var(--orange)" stroke-width="1.8" fill="none"/></svg></div>
    <p>Email:<br>info@vertexgroup.example</p>
  </div>

  <div class="abs" style="left:95px;top:4560px;width:1010px;height:1px;background:rgba(255,255,255,.35)"></div>
  <p class="abs" style="left:0;top:4590px;width:1200px;text-align:center;font-size:14px;color:#fff">Copyright © 2025 All rights are reserved.</p>
</footer>

</body>
</html>
```